Business Card Design

I need a business card for a company based in London, UK. I provide garden design, landscaping and maintenance services. The company specialises in modern, urban gardens. It must be horizontal design, white paper and black simple (easy to read) font. The print must be on clear, white surrounding. I like design that use the colours black, yellow, grey and different shades of green. The design must be tidy. It must not be overloaded with decorating. Embodied a small picture of a fragment of garden or plant or leaf in the sun (it must be yellowish and greenish). It would be good if it's "live and energetic". I attached all text and logo that have to appear on the card.

Target Market(s)

architect, property designers, property management companies, large property owners

Industry/Entity Type

Landscaping

Contact Information for Business Card

All the text must be the same as on my old card which I attached.

Requirements
Must have
• modern, simple, tidy, professional look
green, yellow, black colours,
white surrounding,
simple readable black font on clear white surrounding,
a small picture of garden or plant or "sun lights through the tree canopy"
Nice to have
• graduate movement from light green to dark green
Should not have
• old style font,
text must no be placed on pictures or decorations,
red and blue colours,
picture on the reverse

```html
<!DOCTYPE html>
<html lang="en">
<head>
<meta charset="utf-8">
<title>Fieldrow Gardens – Business Card Concepts</title>
<link href="https://fonts.googleapis.com/css2?family=Open+Sans:wght@400;600;700&family=Roboto+Condensed:wght@400;700&display=swap" rel="stylesheet">
<style>
  :root {
    --backdrop: #2e2e2e;
    --paper: #ffffff;
    --ink: #3a3a3a;
    --ink-soft: #6a6a6a;
    --green-deep: #1f9a55;
    --green-tagline: #2aa55c;
    --green: #8cc63f;
    --green-mid: #a9d46a;
    --green-light: #cfe6a6;
    --green-pale: #eaf4da;
    --yellow: #f6ec1c;
    --body-font: "Open Sans", sans-serif;
    --list-font: "Roboto Condensed", sans-serif;
  }
  * { box-sizing: border-box; margin: 0; padding: 0; }
  html, body { width: 1200px; height: 1200px; overflow: hidden; }
  body {
    background: var(--backdrop);
    font-family: var(--body-font);
    color: var(--ink);
    display: grid;
    grid-template-columns: 600px 600px;
    grid-template-rows: 600px 600px;
  }
  .concept {
    display: flex;
    flex-direction: column;
    align-items: center;
    justify-content: center;
    gap: 20px;
  }
  .card {
    position: relative;
    width: 460px;
    height: 270px;
    background: var(--paper);
    overflow: hidden;
  }

  /* ---------- Reverse: service list ---------- */
  .services { padding: 16px 0 0; list-style: none; }
  .service { margin-bottom: 9px; }
  .service__title {
    font-family: var(--list-font);
    font-weight: 700;
    font-size: 12px;
    color: var(--green-deep);
    text-transform: uppercase;
    letter-spacing: 0.2px;
    line-height: 20px;
    padding-left: 22px;
  }
  .service__detail {
    font-family: var(--list-font);
    font-size: 11.5px;
    color: var(--ink);
    line-height: 19px;
    padding-left: 22px;
  }
  .card--back-bands .service__title { background: var(--green); color: #1d5d2e; width: 150px; }
  .card--back-bands .service__detail { background: var(--green-pale); }
  .card--back-tinted { background: var(--green-light); }
  .card--back-tinted .services { padding-top: 12px; }
  .card--back-tinted .service__title { background: var(--green); color: #1d5d2e; }
  .card--back-tinted .service__detail { background: var(--green-pale); }
  .card--back-bullets .service { position: relative; }
  .card--back-bullets .service::before {
    content: "";
    position: absolute;
    left: 10px; top: 6px;
    width: 7px; height: 22px;
    background: var(--green);
  }

  /* ---------- Shared front parts ---------- */
  .logo {
    position: absolute;
    top: 24px; right: 22px;
    display: flex;
    align-items: center;
    gap: 7px;
    font-size: 15px;
    font-weight: 400;
    color: var(--ink-soft);
    letter-spacing: 0.2px;
  }
  .logo__square { width: 11px; height: 11px; background: var(--green); }
  .owner {
    position: absolute;
    top: 22px; left: 34px;
    font-size: 10px;
    line-height: 13px;
    color: var(--ink-soft);
  }
  .tagline {
    position: absolute;
    top: 78px; left: 26px;
    font-size: 14px;
    font-weight: 600;
    color: var(--green-tagline);
    letter-spacing: 0.2px;
  }
  .contacts {
    position: absolute;
    top: 128px; left: 34px;
    font-size: 12px;
    line-height: 15px;
    color: var(--ink);
  }

  /* ---------- Front A: colour blocks ---------- */
  .card--blocks .edge { position: absolute; left: 0; top: 0; bottom: 0; width: 8px; background: var(--green-deep); }
  .card--blocks .services-line {
    position: absolute;
    top: 60px; left: 38px;
    font-size: 17px;
    font-weight: 600;
    line-height: 20px;
    color: #4a4a4a;
  }
  .card--blocks .person {
    position: absolute;
    top: 186px; left: 38px;
    font-size: 14px;
    font-weight: 700;
    color: #4a4a4a;
  }
  .card--blocks .logo { top: 16px; }
  .info-column {
    position: absolute;
    right: 0; top: 50px; bottom: 0;
    width: 190px;
    display: flex;
    flex-direction: column;
  }
  .info-block {
    position: relative;
    padding: 12px 14px;
    font-size: 11.5px;
    line-height: 14px;
    color: #2f2f2f;
  }
  .info-block svg { position: absolute; right: 12px; bottom: 10px; }
  .info-block--address { background: var(--yellow); height: 76px; }
  .info-block--phone { background: var(--green-light); height: 70px; }
  .info-block--web { background: var(--green); height: 74px; padding-top: 30px; }

  /* ---------- Front B / D: artwork corner ---------- */
  .art-tree {
    position: absolute;
    right: 12px; bottom: 8px;
    width: 118px; height: 108px;
    border-radius: 50% 50% 40% 50%;
    background: radial-gradient(circle at 55% 40%, var(--green-mid), var(--green) 55%, var(--green-deep));
  }
  .art-swirl {
    position: absolute;
    right: 10px; bottom: 6px;
    width: 150px; height: 140px;
    border-radius: 50%;
    background: radial-gradient(circle at 50% 50%, var(--green-pale), var(--green-light) 55%, var(--green-mid));
  }

  /* ---------- Front C: swoosh ---------- */
  .swoosh { position: absolute; left: 0; top: 0; }
  .card--swoosh .contacts { top: 142px; left: 30px; color: #2f3a23; }
</style>
</head>
<body>

  <!-- Concept 1 -->
  <section class="concept">
    <article class="card card--back-bands" aria-label="Card reverse, service list">
      <ul class="services">
        <li class="service"><div class="service__title">Garden Design</div><div class="service__detail">all styles: hand-drawn &amp; CAD, detailed mapping, underground service tracing, soil analysis</div></li>
        <li class="service"><div class="service__title">Garden Maintenance</div><div class="service__detail">lawn care programs, improving soil, planting, root health issues, clearance, tree husbandry</div></li>
        <li class="service"><div class="service__title">Ground Maintenance</div><div class="service__detail">algae, moss &amp; pest control, paths, driveways, terraces, car parks, playgrounds</div></li>
        <li class="service"><div class="service__title">Patios, Fences &amp; Decking</div><div class="service__detail">railings, walls, gates, paving and timber decking repairs</div></li>
        <li class="service"><div class="service__title">Ponds &amp; Water Features</div><div class="service__detail">rockeries, pumps, filters and lighting</div></li>
      </ul>
    </article>
    <article class="card card--blocks" aria-label="Card front, colour blocks">
      <div class="edge"></div>
      <div class="logo"><span class="logo__square"></span>fieldrow gardens</div>
      <p class="services-line">design<br>landscaping<br>maintenance</p>
      <p class="person">Tomas Hale</p>
      <div class="info-column">
        <div class="info-block info-block--address">42 Mill Lane,<br>Kingsford, KF4 2QT
          <svg width="22" height="20" viewBox="0 0 22 20" aria-hidden="true"><path d="M11 1 L21 10 H18 V19 H13 V13 H9 V19 H4 V10 H1 Z" fill="#fff"/></svg>
        </div>
        <div class="info-block info-block--phone">02071234567<br>07700900123
          <svg width="12" height="22" viewBox="0 0 12 22" aria-hidden="true"><rect x="1" y="1" width="10" height="20" rx="2" fill="none" stroke="#fff" stroke-width="1.6"/><rect x="3" y="4" width="6" height="6" fill="#fff"/><circle cx="6" cy="16" r="1.4" fill="#fff"/></svg>
        </div>
        <div class="info-block info-block--web">www.fieldrow-gardens.co.uk<br>info@fieldrow-gardens.co.uk
          <svg width="20" height="14" viewBox="0 0 20 14" aria-hidden="true" style="top:8px;bottom:auto"><rect x="1" y="1" width="18" height="12" fill="none" stroke="#fff" stroke-width="1.5"/><path d="M1 1 L10 8 L19 1" fill="none" stroke="#fff" stroke-width="1.5"/></svg>
        </div>
      </div>
    </article>
  </section>

  <!-- Concept 2 -->
  <section class="concept">
    <article class="card card--back-tinted" aria-label="Card reverse, service list on green">
      <ul class="services">
        <li class="service"><div class="service__title">Garden Design</div><div class="service__detail">all styles: hand-drawn &amp; CAD, detailed mapping, underground service tracing, soil analysis</div></li>
        <li class="service"><div class="service__title">Garden Maintenance</div><div class="service__detail">lawn care programs, improving soil, planting, root health issues, clearance, tree husbandry</div></li>
        <li class="service"><div class="service__title">Ground Maintenance</div><div class="service__detail">algae, moss &amp; pest control, paths, driveways, terraces, car parks, playgrounds</div></li>
        <li class="service"><div class="service__title">Patios, Fences &amp; Decking</div><div class="service__detail">railings, walls, gates, paving and timber decking repairs</div></li>
        <li class="service"><div class="service__title">Ponds &amp; Water Features</div><div class="service__detail">rockeries, pumps, filters and lighting</div></li>
      </ul>
    </article>
    <article class="card card--tree" aria-label="Card front with tree artwork">
      <p class="owner">Tomas Hale<br>42 Mill Lane, Kingsford, KF4 2QT</p>
      <div class="logo"><span class="logo__square"></span>fieldrow gardens</div>
      <p class="tagline">design | landscaping | maintenance</p>
      <p class="contacts">www.fieldrow-gardens.co.uk<br>02071234567<br>07700900123<br>info@fieldrow-gardens.co.uk</p>
      <div class="art-tree" role="img" aria-label="Illustration of a small tree with bright green leaves"></div>
    </article>
  </section>

  <!-- Concept 3 -->
  <section class="concept">
    <article class="card card--back-bullets" aria-label="Card reverse, service list with bullets">
      <ul class="services">
        <li class="service"><div class="service__title">Garden Design</div><div class="service__detail">all styles: hand-drawn &amp; CAD, detailed mapping, underground service tracing, soil analysis</div></li>
        <li class="service"><div class="service__title">Garden Maintenance</div><div class="service__detail">lawn care programs, improving soil, planting, root health issues, clearance, tree husbandry</div></li>
        <li class="service"><div class="service__title">Ground Maintenance</div><div class="service__detail">algae, moss &amp; pest control, paths, driveways, terraces, car parks, playgrounds</div></li>
        <li class="service"><div class="service__title">Patios, Fences &amp; Decking</div><div class="service__detail">railings, walls, gates, paving and timber decking repairs</div></li>
        <li class="service"><div class="service__title">Ponds &amp; Water Features</div><div class="service__detail">rockeries, pumps, filters and lighting</div></li>
      </ul>
    </article>
    <article class="card card--swoosh" aria-label="Card front with green swoosh">
      <svg class="swoosh" width="460" height="270" viewBox="0 0 460 270" aria-hidden="true">
        <defs>
          <linearGradient id="swoosh-fill" x1="0" y1="1" x2="1" y2="0">
            <stop offset="0" stop-color="#8cc63f"/>
            <stop offset="1" stop-color="#cfe6a6"/>
          </linearGradient>
        </defs>
        <path d="M0 132 Q140 112 340 118 Q262 170 206 270 L0 270 Z" fill="url(#swoosh-fill)"/>
      </svg>
      <p class="owner">Tomas Hale<br>42 Mill Lane, Kingsford, KF4 2QT</p>
      <div class="logo"><span class="logo__square"></span>fieldrow gardens</div>
      <p class="tagline">design | landscaping | maintenance</p>
      <p class="contacts">www.fieldrow-gardens.co.uk<br>02071234567<br>07700900123<br>info@fieldrow-gardens.co.uk</p>
    </article>
  </section>

  <!-- Concept 4 -->
  <section class="concept">
    <article class="card card--back-bullets" aria-label="Card reverse, service list with bullets">
      <ul class="services">
        <li class="service"><div class="service__title">Garden Design</div><div class="service__detail">all styles: hand-drawn &amp; CAD, detailed mapping, underground service tracing, soil analysis</div></li>
        <li class="service"><div class="service__title">Garden Maintenance</div><div class="service__detail">lawn care programs, improving soil, planting, root health issues, clearance, tree husbandry</div></li>
        <li class="service"><div class="service__title">Ground Maintenance</div><div class="service__detail">algae, moss &amp; pest control, paths, driveways, terraces, car parks, playgrounds</div></li>
        <li class="service"><div class="service__title">Patios, Fences &amp; Decking</div><div class="service__detail">railings, walls, gates, paving and timber decking repairs</div></li>
        <li class="service"><div class="service__title">Ponds &amp; Water Features</div><div class="service__detail">rockeries, pumps, filters and lighting</div></li>
      </ul>
    </article>
    <article class="card card--swirl" aria-label="Card front with swirl artwork">
      <p class="owner">Tomas Hale<br>42 Mill Lane, Kingsford, KF4 2QT</p>
      <div class="logo"><span class="logo__square"></span>fieldrow gardens</div>
      <p class="tagline">design | landscaping | maintenance</p>
      <p class="contacts">www.fieldrow-gardens.co.uk<br>02071234567<br>07700900123<br>info@fieldrow-gardens.co.uk</p>
      <div class="art-swirl" role="img" aria-label="Decorative green swirling plant ornament"></div>
    </article>
  </section>

</body>
</html>
```